Elegant Business Cards & Letterhead

We will need the following that need to be designed: Letterhead and Business Cards, there winer will be re-hired for the balance of our stationary needs. Text for the cards and letterheads:

- Corporate Card instead of name
- landline: +971 (4) 362 7041
- mobile: +971 56 2819 605
- 800TUTOR
- email: dubai@velmora-lune.com
- www.velmora-lune.com
- PO Box 387261
Address: Castellan Heights Suite 1708, Dubai UAE

Thank you

Target Market(s)

VIPs, HNWI, High-end Families.

Industry/Entity Type

Luxury Market

Font styles to use
Other font styles liked:
• as explained

Colors

Designer to choose only greyscale colors for use in the design.

Requirements
Must have
• Elegant, Simple, Luxurious, Minimalistic
Nice to have
• Luxury, Golds, Engravings,
Should not have
• Much colors, funky,

```html
<!DOCTYPE html>
<html lang="en">
<head>
<meta charset="utf-8">
<title>Velmora Lune — Business Card</title>
<link rel="stylesheet" href="https://fonts.googleapis.com/css2?family=Marcellus&family=Montserrat:wght@400&display=swap">
<style>
  :root {
    --backdrop: #eeeeee;
    --card-dark: #2b2b2b;
    --card-light: #ececeb;
    --gold: #b48a45;
    --ink: #1e1e1e;
  }
  html, body {
    margin: 0;
    padding: 0;
    overflow: hidden;
  }
  .canvas {
    position: relative;
    width: 1200px;
    height: 934px;
    background: var(--backdrop);
    overflow: hidden;
  }
  .card {
    position: absolute;
    left: 389px;
    width: 418px;
    height: 241px;
    box-sizing: border-box;
  }
  .card--front {
    top: 166px;
    background: var(--card-dark);
    display: flex;
    align-items: center;
    justify-content: center;
  }
  .card--back {
    top: 532px;
    background: var(--card-light);
    text-align: center;
  }
  .wordmark {
    font-family: "Marcellus", serif;
    color: var(--gold);
    letter-spacing: 0.02em;
    white-space: nowrap;
    margin: 0;
    font-weight: 400;
  }
  .card--front .wordmark {
    font-size: 37px;
    margin-top: 2px;
  }
  .card--back .wordmark {
    font-size: 22px;
    padding-top: 24px;
  }
  .contact {
    list-style: none;
    margin: 40px 0 0;
    padding: 0;
    color: var(--ink);
    font-family: "Montserrat", sans-serif;
    font-size: 10.5px;
    line-height: 18.5px;
  }
  .contact .label {
    font-family: "Marcellus", serif;
    font-size: 9px;
    text-transform: uppercase;
    margin-right: 2px;
  }
  .contact .upper {
    text-transform: uppercase;
  }
  .contact .web {
    font-family: "Marcellus", serif;
    font-size: 10px;
    text-transform: uppercase;
    letter-spacing: 0.02em;
  }
  .contact .gap {
    margin-top: 2px;
  }
</style>
</head>
<body>
<main class="canvas">
  <section class="card card--front">
    <h1 class="wordmark">VELMORA LUNE</h1>
  </section>

  <section class="card card--back">
    <h2 class="wordmark">VELMORA LUNE</h2>
    <ul class="contact">
      <li><span class="label">Phone</span> +971 (4) 362 7041</li>
      <li><span class="label">Mobile</span> +971 56 2819 605</li>
      <li>800TUTOR</li>
      <li><span class="label">Email</span> <span class="upper">newyork@velmora-lune.com</span></li>
      <li class="upper gap">PO Box 387261</li>
      <li class="upper">Castellan Heights Suite 1708, Dubai UAE</li>
      <li class="web">www.velmora-lune.com</li>
    </ul>
  </section>
</main>
</body>
</html>
```